I need a business card design for a new company that will be doing consulting work around issues of cultural competency, and diversity and inclusion. I would like the design to be crisp and clear with bold but conservative colors and incorporate shades of blue

Target Market(s)

Small businesses, schools, non-profits

Industry/Entity Type

Consulting

Font styles to use
Serif
Sans Serif

Colors
0c5ba6
6b449b
3276b5
0292cd

Requirements
Must have
• A Morrow Venture (name of company)
• Lemlem Tavish
• CEO
• lemlem@amorrowventure.com
• (215)483-2756

```html
<!DOCTYPE html>
<html lang="en">
<head>
<meta charset="utf-8">
<title>A Morrow Venture – Business Card</title>
<link rel="stylesheet" href="https://fonts.googleapis.com/css2?family=Russo+One&family=Open+Sans:wght@400&display=swap">
<style>
  :root {
    --page: #ffffff;
    --frame-line: #8a8a8a;
    --card-blue: #343c8e;
    --stripe-dark: #27246a;
    --text-blue: #2a62b0;
    --text-shadow: #1d1a3f;
  }
  html, body {
    margin: 0;
    padding: 0;
    width: 1200px;
    height: 1200px;
    overflow: hidden;
    background: var(--page);
  }
  .canvas {
    position: relative;
    width: 1200px;
    height: 1200px;
  }
  .card-frame {
    position: absolute;
    left: 125px;
    top: 302px;
    width: 950px;
    height: 596px;
    border: 1px solid var(--frame-line);
    box-sizing: border-box;
    background: var(--page);
  }
  .card {
    position: absolute;
    left: 145px;
    top: 323px;
    width: 910px;
    height: 556px;
    border-radius: 12px;
    background: var(--card-blue);
    overflow: hidden;
  }
  .card-stripes {
    position: absolute;
    inset: 0;
  }
  .card-text {
    position: absolute;
    margin: 0;
    line-height: 1;
    white-space: nowrap;
    font-family: "Open Sans", sans-serif;
    font-weight: 400;
    color: var(--text-blue);
    text-shadow: 2px 2px 0 var(--text-shadow);
  }
  .company-name {
    left: 0;
    width: 820px;
    text-align: center;
    top: 92px;
    font-family: "Russo One", sans-serif;
    font-size: 60px;
    letter-spacing: 2px;
    text-shadow: none;
  }
  .contact {
    position: absolute;
    left: 50px;
    top: 0;
    width: 375px;
    text-align: center;
  }
  .person-name { left: 0; width: 375px; top: 360px; font-size: 44px; letter-spacing: -1px; }
  .person-role { left: 0; width: 375px; top: 415px; font-size: 24px; }
  .person-email { left: 0; width: 375px; top: 452px; font-size: 29px; letter-spacing: -1px; }
  .person-phone { left: 0; width: 375px; top: 490px; font-size: 29px; letter-spacing: -1px; }
  .website {
    right: 30px;
    top: 512px;
    font-size: 25px;
    letter-spacing: -0.5px;
  }
</style>
</head>
<body>
<div class="canvas">
  <div class="card-frame"></div>
  <div class="card">
    <svg class="card-stripes" width="910" height="556" viewBox="0 0 910 556" aria-hidden="true">
      <polygon points="807,0 845,0 637,338 600,338" fill="var(--stripe-dark)"/>
      <polygon points="577,375 910,375 910,391 602,391 503,556 465,556" fill="var(--stripe-dark)"/>
    </svg>

    <h1 class="card-text company-name">A Morrow Venture</h1>

    <div class="contact">
      <p class="card-text person-name">Lemlem Tavish</p>
      <p class="card-text person-role">CEO</p>
      <p class="card-text person-email">lemlem@amorrowventure.com</p>
      <p class="card-text person-phone">(215)483-2756</p>
    </div>

    <p class="card-text website">www.amorrowventure.com</p>
  </div>
</div>
</body>
</html>
```